Flyer to be utilised on social media and email marketing - Making Divorce Applications Affordable

Finalising Your Divorce Made Easy <br/><br/>Are you separated and both seeking to Divorce? At Brellis & Brellis Legal we provide a cost effective way for this to occur.... <br/><br/>OLD APPROACH <br/> Arrange a meeting with a solicitor <br/> Attend appointment <br/> Provide background information to the lawyer <br/> Lawyer to draft document <br/> Lawyer to contact you to obtain further instructions, if required <br/>Lawyer to amend divorce application, if further amendments required <br/> Lawyer to send you a copy of the draft Divorce Application<br/>Lawyer to make further changes, if required <br/>Lawyer to resend you draft Divorce Application, if required <br/>Lawyer to organise an appointment to attend office to sign Divorce Application <br/>TIME CONSUMING & COSTLY - CAN COST OVER $3500 <br/><br/>NEW APPROACH <br/> We send you a Form <br/> You complete the Form <br/> We review your instructions <br/>We provide you with advicee <br/>We draft Divorce Application and send to you for review <br/> QUICK & SIMPLE PROCESS - FIXED COST OF $799 INCLUSIVE OF GST <br/><br/>Please include the OLD APPROACH ON THE LEFT SIDE AND NEW APPROACH ON THE RIGHT SIDE OF THE PAGE (SO THAT THEY ARE NEXT TO EACH OTHER)<br/><br/>*Terms and Conditions - Applies to simple joint divorce applications, no court appearances, no drafting or finalising any further court documentations, and excludes disbursements costs including court filing fee <br/>

Target Market(s)

Separated Families - Individuals from 35+

Industry/Entity Type

Legal

Font styles to use
Serif

Colors
0255a3

Requirements
Must have
• Please include website - www.brellisandbrellislegal.com.au
• Email - office@brellisandbrellislegal.com.au
• Logo Colour - Royal blue colour #10416a or hex code #063169

```html
<!DOCTYPE html>
<html lang="en">
<head>
<meta charset="utf-8">
<title>Brellis &amp; Brellis Legal – Amicable Divorce</title>
<link rel="stylesheet" href="https://fonts.googleapis.com/css2?family=Playfair+Display:wght@400;700&family=Crimson+Text:wght@400;600&display=swap">
<style>
  :root {
    --royal: #10416a;
    --navy: #0a4378;
    --band: rgba(14, 56, 104, 0.9);
    --orange: #f7941d;
    --ink: #3f3f45;
    --mist: #f1f1f3;
    --white: #ffffff;
    --photo-dark: #2b2b2d;
    --photo-mid: #4a4a4e;
  }
  * { margin: 0; padding: 0; box-sizing: border-box; }
  html, body { width: 844px; height: 1200px; overflow: hidden; background: var(--white); }
  .flyer { position: relative; width: 844px; height: 1200px; overflow: hidden; font-family: "Crimson Text", Georgia, serif; color: var(--ink); }

  .hero { position: absolute; left: 0; top: 0; width: 844px; height: 665px; }

  .brand { position: absolute; left: 572px; top: 0; width: 270px; height: 87px; background: var(--navy);
    display: flex; flex-direction: column; align-items: center; justify-content: center; }
  .brand-name { font-family: "Crimson Text", Georgia, serif; color: var(--white); font-size: 21px; font-weight: 400;
    letter-spacing: 0.5px; text-transform: uppercase; text-align: center; line-height: 1.1; }

  .headline-band { position: absolute; left: 0; top: 350px; width: 844px; height: 141px; background: var(--band);
    text-align: center; color: var(--white); padding-top: 13px; }
  .headline { font-family: "Playfair Display", Georgia, serif; font-weight: 700; line-height: 1; }
  .headline .line-a { display: block; font-size: 37px; letter-spacing: 0.3px; }
  .headline .line-b { display: block; font-size: 47px; margin-top: 4px; letter-spacing: 0.3px; }
  .tagline { font-family: "Crimson Text", Georgia, serif; font-size: 18px; margin-top: 10px; }

  .approach { position: absolute; }
  .approach h2 { font-family: "Playfair Display", Georgia, serif; font-weight: 700; color: var(--royal);
    font-size: 36px; line-height: 1.02; }
  .approach ul { list-style: none; }
  .approach li { position: relative; padding-left: 15px; font-size: 15.5px; line-height: 1.08; }
  .approach li::before { content: ""; position: absolute; left: 0; top: 6px; width: 5px; height: 5px; border-radius: 50%; background: var(--ink); }
  .approach li.key { font-family: "Playfair Display", Georgia, serif; font-weight: 700; font-size: 14px; }
  .approach li.cost { text-transform: uppercase; font-size: 14px; }
  .price { display: block; font-family: "Playfair Display", Georgia, serif; font-weight: 700; color: var(--orange);
    font-size: 23px; text-transform: none; margin-top: 4px; }

  .approach-old { left: 29px; top: 614px; width: 390px; }
  .approach-old ul { margin-top: 16px; }
  .approach-old li { margin-bottom: 9px; }

  .approach-new { left: 464px; top: 708px; width: 370px; }
  .approach-new h2 { padding-left: 0; }
  .approach-new h2 span { display: block; padding-left: 6px; }
  .approach-new ul { margin-top: 17px; padding-left: 3px; }
  .approach-new li { margin-bottom: 12px; }
  .approach-new li::before { background: var(--navy); }

  .call-band { position: absolute; left: 0; top: 1024px; width: 844px; height: 50px; background: var(--mist);
    display: flex; align-items: center; justify-content: center; }
  .call { font-family: "Playfair Display", Georgia, serif; font-weight: 700; color: var(--royal); font-size: 25px; }

  .contact-band { position: absolute; left: 0; top: 1074px; width: 844px; height: 43px; background: var(--navy);
    color: var(--white); font-size: 15.5px; }
  .contact { position: absolute; top: 0; height: 43px; display: flex; align-items: center; gap: 10px; }
  .contact-web { left: 91px; }
  .contact-mail { left: 470px; }

  .terms { position: absolute; left: 48px; top: 1124px; width: 748px; text-align: center; }
  .terms h3 { font-family: "Crimson Text", Georgia, serif; font-weight: 400; font-size: 15px; color: var(--ink); }
  .terms p { font-size: 10.3px; line-height: 1.15; color: var(--ink); margin-top: 2px; }
</style>
</head>
<body>
<main class="flyer">
  <svg class="hero" viewBox="0 0 844 665" xmlns="http://www.w3.org/2000/svg">
    <defs>
      <linearGradient id="portraitTone" x1="0" y1="0" x2="1" y2="1">
        <stop offset="0" stop-color="#3a3a3c"/>
        <stop offset="0.5" stop-color="#26262a"/>
        <stop offset="1" stop-color="#55555a"/>
      </linearGradient>
    </defs>
    <polygon role="img" aria-label="Photograph of a smiling professional woman in a dark suit holding a folder"
      points="0,0 844,0 844,510 420,642 0,510" fill="url(#portraitTone)"/>
    <polygon class="chevron" points="112,546 112,563 420,662 727,563 727,546 420,642" fill="#0a4378"/>
  </svg>

  <div class="brand">
    <span class="brand-name">Brellis &amp; Brellis Legal</span>
  </div>

  <section class="headline-band">
    <h1 class="headline">
      <span class="line-a">SEPARATED AND SEEKING AN</span>
      <span class="line-b">AMICABLE DIVORCE?</span>
    </h1>
    <p class="tagline">At Brellis &amp; Brellis Legal we provide a cost effective way for this to occur....</p>
  </section>

  <section class="approach approach-old">
    <h2>Old Face to<br>Face Approach</h2>
    <ul>
      <li>Arrange a meeting with a lawyer</li>
      <li>Attend appointment with a lawyer</li>
      <li>Provide information to the lawyer</li>
      <li>Lawyer to draft the Application for Divorce</li>
      <li>Meeting with a lawyer to confirm your instructions in Divorce Application</li>
      <li>Lawyer to amend Divorce Application, if required</li>
      <li>Lawyer to provide you with final Divorce Application</li>
      <li>Meeting with lawyer for you to sign Divorce Application</li>
      <li class="key">Process can take up to 6 months or longer</li>
      <li class="cost">Time consuming &amp; costly –<span class="price">OVER $3500+</span></li>
    </ul>
  </section>

  <section class="approach approach-new">
    <h2>New Online<span>Approach</span></h2>
    <ul>
      <li>We send you a form to complete Online</li>
      <li>We review your instructions and provide you with legal advice</li>
      <li>We prepare the Divorce Application</li>
      <li>We file your Divorce Application on your behalf</li>
      <li class="key">Finalised within 24 hours</li>
      <li class="cost">Quick, simple &amp; affordable –<span class="price">$799* Fixed Fee</span></li>
    </ul>
  </section>

  <div class="call-band">
    <p class="call">Call Us: 1300 555 014</p>
  </div>

  <div class="contact-band">
    <div class="contact contact-web">
      <svg width="24" height="24" viewBox="0 0 24 24" aria-hidden="true">
        <g fill="none" stroke="#fff" stroke-width="1.6">
          <circle cx="12" cy="12" r="10.5"/>
          <ellipse cx="12" cy="12" rx="4.5" ry="10.5"/>
          <line x1="1.5" y1="12" x2="22.5" y2="12"/>
          <line x1="3.5" y1="6.5" x2="20.5" y2="6.5"/>
          <line x1="3.5" y1="17.5" x2="20.5" y2="17.5"/>
        </g>
      </svg>
      <span>www.brellisandbrellislegal.com.au</span>
    </div>
    <div class="contact contact-mail">
      <svg width="28" height="20" viewBox="0 0 28 20" aria-hidden="true">
        <g fill="none" stroke="#fff" stroke-width="1.8">
          <rect x="1" y="1" width="26" height="18"/>
          <polyline points="1,1 14,11 27,1"/>
          <line x1="1" y1="19" x2="11" y2="9"/>
          <line x1="27" y1="19" x2="17" y2="9"/>
        </g>
      </svg>
      <span>office@brellisandbrellislegal.com.au</span>
    </div>
  </div>

  <section class="terms">
    <h3>*Terms and Conditions</h3>
    <p>Fixed Fee applies only to simple joint divorce applications; not applicable to court appearances; does not include drafting or finalising court documentation (other than simple divorce application); excludes disbursements costs including court filing fee; timeframe to finalise is subject to receipt of instructions and documentation and relates to filing of divorce application, not timeframe for Divorce Order</p>
  </section>
</main>
</body>
</html>
```